Flyer-Design für Zweithaar Studio
Zielgruppe
Firma MOLVA Ketz ist ein Zweithaar Studio. Hier erhalten Kunden individuell auf sie zugeschnittene Perücken und Toupets. Unsere Zielgruppe sind Männer und Frauen mit wenig oder keiner Kopfbehaarung oder Menschen die krankheitsbedingt unter Haarausfall leiden.
Aufgabenstellung
Bitte Vorschläge zu Anzahl Seiten und Format erstellen, aktuell haben wir noch keine Vorstellung dazu. Folgende Inhalte haben wir schon mal als Entwurf vorbereitet:
Eine Seite zum Thema Toupets mit dem Bild vom Mann:
Leiden Sie an übermäßigem Haarausfall?
Fühlen Sie sich nicht mehr 100% wohl damit und möchten gerne wieder Ihre Attraktivität und vor allem das Wohlbefinden steigern?
Dann sind Sie bei uns sehr gut aufgehoben, denn wir können Ihnen Ihr Toupet individuell auf Ihre Bedürfnisse hin z.B. Farbe, Grauanteil, Größe und Styling anpassen.
Eine Seite zum Thema Perücken mit dem Bild der Frau:
Sind Sie an einer Perücke interessiert die augenscheinlich keinen Unterschied zu gewachsenem Haar aufweist?
Dann sind Sie bei uns an der richtigen Adresse. Die langjährige Erfahrung im Zweithaar Bereich von Friseurmeisterin verspricht Ihnen optimale Beratung und ein individuell auf Sie abgestimmtes Produkt.
Bei uns erhalten Sie Zugriff auf verschiedene Modelle im gesamten Preisspektrum.
Liegt eine von Ihrem Arzt attestierte Erkrankung vor, übernimmt Ihre Krankenkasse höchstwahrscheinlich die Kosten für Ihr Zweithaar. Die Formalitäten dazu erledigen wir gerne für Sie um Ihnen unnötigen Stress zu ersparen.
Eine weitere Seite mit den besonderen Merkmalen mit dem Bild Diversity:
Mit unserer Befestigungsmethode sind Sie sehr flexibel - starker halt für jede Situation und auf Wunsch auch abnehmbar z.B. nachts beim schlafen.
Der große Vorteil unserer Befestigungsmethode liegt darin, dass Sie diese selbst umsetzen können und somit nicht jeden Monat das Studio zur Neubefestigung aufsuchen müssen. Das spart Ihnen Zeit und Geld.
Wir können Ihnen Toupets und Perücken in allen Preisklassen anbieten, in verschiedenen Farben, auf Wunsch mit Grauanteil passend zum Alter des Trägers. Unsere Friseurmeisterin Frau Tiltrop berät Sie gerne, natürlich unverbindlich und kostenlos.

```html
<!DOCTYPE html>
<html lang="de">
<head>
<meta charset="utf-8">
<title>MOLVA Ketz – Flyer Zweithaar Studio</title>
<link rel="stylesheet" href="https://fonts.googleapis.com/css2?family=Libre+Bodoni:wght@700&family=Roboto:wght@300;400&display=swap">
<style>
  :root {
    --stage: #d9dadb;
    --paper: #f3f2ef;
    --slate: #4b4e50;
    --olive: #4f473a;
    --charcoal: #2c2b2a;
    --maroon: #5b2424;
    --ink-light: #f4f1ea;
    --ink-dark: #3a3a3a;
    --serif: "Libre Bodoni", "Bodoni Moda", serif;
    --sans: "Roboto", "Helvetica Neue", Arial, sans-serif;
  }
  * { box-sizing: border-box; margin: 0; padding: 0; }
  html, body {
    width: 1200px; height: 3170px; overflow: hidden;
    background: var(--stage);
  }
  .flyer-spread {
    position: absolute; left: 260px;
    width: 680px; height: 730px;
    display: flex;
    box-shadow: 0 18px 30px rgba(0,0,0,.18);
  }
  .spread-outside-back { top: 50px; }
  .spread-outside-toupet { top: 830px; }
  .spread-inside-wig { top: 1610px; }
  .spread-inside-benefits { top: 2390px; }

  .panel {
    position: relative; width: 340px; height: 730px; overflow: hidden;
    color: var(--ink-light);
  }
  .panel + .panel { box-shadow: inset 1px 0 0 rgba(0,0,0,.25); }

  .photo { position: absolute; left: 0; width: 100%; }

  .headline {
    font-family: var(--serif); font-weight: 700;
    font-size: 40px; line-height: .95; letter-spacing: 2px;
    text-transform: uppercase;
  }
  .subline {
    font-family: var(--sans); font-weight: 300;
    font-size: 26px; line-height: 1.15;
  }
  .body-copy {
    font-family: var(--sans); font-weight: 300;
    font-size: 13.5px; line-height: 1.55;
  }

  /* Kontakt panel */
  .panel-contact { background: var(--slate); }
  .contact-area {
    position: absolute; top: 0; left: 0; width: 100%; height: 420px;
    background: var(--paper); color: var(--ink-dark);
    padding: 110px 34px 0 0; text-align: right;
  }
  .contact-title {
    font-family: var(--sans); font-weight: 300; font-size: 30px;
    margin-bottom: 22px;
  }
  .contact-lines { list-style: none; font-family: var(--sans); font-weight: 300; font-size: 13.5px; line-height: 1.9; }
  .brand-name {
    position: absolute; left: 0; right: 0; top: 540px; text-align: center;
    font-family: var(--serif); font-weight: 700; font-size: 38px;
    letter-spacing: 2px; color: var(--ink-light);
  }

  /* Cover */
  .panel-cover { background: var(--slate); }
  .panel-cover .photo {
    top: 0; height: 360px;
    background: linear-gradient(160deg, #6b4a34 0%, #2e2220 45%, #1a1718 100%);
  }
  .cover-title { position: absolute; top: 420px; left: 0; right: 0; text-align: center; }
  .cover-title .subline { margin-top: 6px; }

  /* Toupets flap */
  .panel-toupet-flap { background: var(--olive); }
  .panel-toupet-flap .photo {
    top: 0; height: 440px;
    background: linear-gradient(180deg, #1f1f22 0%, #131418 60%, #1b1b1e 100%);
  }
  .flap-title { position: absolute; top: 480px; left: 30px; right: 20px; }
  .flap-title .subline { margin-top: 4px; }

  /* Toupet text */
  .panel-toupet-text { background: var(--olive); }
  .panel-toupet-text .photo {
    top: 0; height: 440px;
    background: linear-gradient(165deg, #1c1a1c 0%, #2b3346 45%, #1b1d26 80%, #141416 100%);
  }
  .panel-toupet-text .body-copy { position: absolute; top: 475px; left: 30px; right: 28px; }

  /* Perücken */
  .panel-wig { background: var(--maroon); }
  .panel-wig .photo {
    top: 0; height: 430px;
    background: radial-gradient(ellipse at 45% 35%, #7a2a22 0%, #3a1a18 35%, #1d1c1c 70%);
  }
  .wig-dark-band { position: absolute; top: 430px; left: 0; width: 100%; height: 10px; background: var(--charcoal); }
  .wig-title { position: absolute; top: 378px; left: 30px; right: 20px; }
  .wig-title .headline { font-size: 36px; }
  .panel-wig .body-copy { position: absolute; top: 505px; left: 30px; right: 26px; }

  .panel-wig-text { background: var(--maroon); }
  .wig-text-top { position: absolute; top: 0; left: 0; width: 100%; height: 440px; background: var(--charcoal); }
  .panel-wig-text .body-copy { position: absolute; top: 470px; left: 28px; right: 28px; }

  /* Warum / benefits */
  .panel-why, .panel-benefits { background: var(--charcoal); }
  .why-title { position: absolute; top: 120px; left: 36px; right: 20px; }
  .why-title .headline { font-size: 34px; }
  .why-title .subline { font-size: 23px; margin-top: 4px; }
  .panel-benefits .body-copy { position: absolute; top: 60px; left: 28px; right: 28px; font-size: 13px; }
  .portrait-strip {
    position: absolute; top: 430px; left: 0; width: 680px; height: 300px;
    background: linear-gradient(90deg, #8a6a52 0%, #c9a58a 18%, #6f5443 33%, #d8b69c 50%, #9c7a60 66%, #e1c3ab 82%, #b8967c 100%);
  }
</style>
</head>
<body>

<section class="flyer-spread spread-outside-back">
  <article class="panel panel-contact">
    <div class="contact-area">
      <h2 class="contact-title">Kontakt</h2>
      <ul class="contact-lines">
        <li>Inhaber Nachname</li>
        <li>Adresszeile 1</li>
        <li>1234 Adresse</li>
        <li>Tel.: 0123 456 789</li>
        <li>info@webadresse.de</li>
        <li>www.webadresse.de</li>
      </ul>
    </div>
    <div class="brand-name">MOLVA KETZ</div>
  </article>
  <article class="panel panel-cover">
    <div class="photo" role="img" aria-label="Foto: elegantes Paar mit vollem Haar vor dunklem Hintergrund"></div>
    <div class="cover-title">
      <h1 class="headline">Volles<br>Haar</h1>
      <p class="subline">mit Zweithaar</p>
    </div>
  </article>
</section>

<section class="flyer-spread spread-outside-toupet">
  <article class="panel panel-toupet-flap">
    <div class="photo" role="img" aria-label="Foto: dunkle Holzwand"></div>
    <div class="flap-title">
      <h2 class="headline">Toupets</h2>
      <p class="subline">zum Wohlfühlen</p>
    </div>
  </article>
  <article class="panel panel-toupet-text">
    <div class="photo" role="img" aria-label="Foto: lächelnder Mann in Lederjacke, sitzend"></div>
    <p class="body-copy">Leiden Sie an übermäßigem Haarausfall? Fühlen Sie sich nicht mehr 100% wohl damit und möchten gerne wieder Ihre Attraktivität und vor allem das Wohlbefinden steigern? Dann sind Sie bei uns sehr gut aufgehoben, denn wir können Ihnen Ihr Toupet individuell auf Ihre Bedürfnisse hin z.B. Farbe, Grauanteil, Größe und Styling anpassen.</p>
  </article>
</section>

<section class="flyer-spread spread-inside-wig">
  <article class="panel panel-wig">
    <div class="photo" role="img" aria-label="Foto: Frau mit wehendem rotem Haar"></div>
    <div class="wig-dark-band"></div>
    <div class="wig-title">
      <h2 class="headline">Perücken</h2>
      <p class="subline">für Natürlichkeit</p>
    </div>
    <p class="body-copy">Sind Sie an einer Perücke interessiert die augenscheinlich keinen Unterschied zu gewachsenem Haar aufweist? Dann sind Sie bei uns an der richtigen Adresse. Die langjährige Erfahrung im Zweithaar Bereich von Friseurmeisterin Ines Tiltrop verspricht Ihnen optimale Beratung und ein individuell auf Sie abgestimmtes Produkt.</p>
  </article>
  <article class="panel panel-wig-text">
    <div class="wig-text-top"></div>
    <p class="body-copy">Bei uns erhalten Sie Zugriff auf verschiedene Modelle im gesamten Preisspektrum. Liegt eine von Ihrem Arzt attestierte Erkrankung vor, übernimmt Ihre Krankenkasse höchstwahrscheinlich die Kosten für Ihr Zweithaar. Die Formalitäten dazu erledigen wir gerne für Sie um Ihnen unnötigen Stress zu ersparen.</p>
  </article>
</section>

<section class="flyer-spread spread-inside-benefits">
  <article class="panel panel-why">
    <div class="why-title">
      <h2 class="headline">Warum</h2>
      <p class="subline">bei uns kaufen?</p>
    </div>
  </article>
  <article class="panel panel-benefits">
    <p class="body-copy">Mit unserer Befestigungsmethode sind Sie sehr flexibel – starker Halt für jede Situation und auf Wunsch auch abnehmbar z.B. nachts beim Schlafen.<br>Der große Vorteil unserer Befestigungsmethode liegt darin, dass Sie diese selbst umsetzen können und somit nicht jeden Monat das Studio zur Neubefestigung aufsuchen müssen. Das spart Ihnen Zeit und Geld.<br>Wir können Ihnen Toupets und Perücken in allen Preisklassen anbieten, in verschiedenen Farben, auf Wunsch mit Grauanteil passend zum Alter des Trägers. Unsere Friseurmeisterin Frau Tiltrop berät Sie gerne, natürlich unverbindlich und kostenlos.</p>
  </article>
  <div class="portrait-strip" role="img" aria-label="Fotostreifen: Porträts verschiedener lächelnder Menschen"></div>
</section>

</body>
</html>
```